QUORVIX - Sydney Based Technology Consultancy -Logo & Business Card design

Who are we?
-
Quorvix is an emerging and advanced technology consulting and professional services business based in Sydney, Australia. Quorvix specialising in increasing value to organisations through the effective use of current and emerging technologies, ensuring that technology is a sustainable catalyst to attaining stated business goals.

We pride ourselves in challenging the norm.

What do we want?
-
We are looking to update our "Brand" we already have a simple “home grown” logo and we are now looking for a new one, once we have this updated logo and businesses look and feel though the business card design we will refresh our website with the new logo and design thus updating the Companies overall look at feel.

Our current site is www.quorvix-example.net.au is a very basic wordpress site and we will be updating it once we have the new logo and designs done

Our initial thoughts on the new Quorvix identity are
• Logo Concept
- One of the key things is obviously the 8
- I was thinking that a logo that had 8 as the core of the logo would be cool,
- Almost like having a “ring” or hoop that is twisted to form an 8 with different services scribed on the inside.
- So we would have a Large 8 and the inside would have ring each service or section engraved.

• Brand / web Feel
- Simple
- Professional
- Innovative
- Clear
- Destination
- Unique
- Impartial
- Safe
- Leading edge
- Familiar

- Emerging technologies
- White and ice / glacier blue
- The familiar feel of the Brindle web site
- Embedded specialist Video clips

• Portfolio of Services
- Quorvix – A smart place for Smart people
- Quorvix – we provide the process to take ideas from awareness to reality
- Focus should be on the brand quality consistent clear local knowledge with regional, national, theatre and global presence

Access to Specialists
- Emerging technologies
- Sustainability
- Collaboration
- Data centre
- Virtualisation

• Adjacent ideas under the one Brand
- Tembrosk – Enable Business Collaboration
- Plinsk – Infrastructure Virtualisation
- morvo - smart people and processes
- skandel - Emerging technologies
- brunhavel - business to technology integration
- tolpin - Smart Infrastructure
- yusk – Connected communities
- dwol - sustainability

Target Market(s)

Australia, New Zealand and Asia pacific organisations that are typically English speaking.
Markets
- IT & Technology partners
- Banking and Finance
- Health

Industry/Entity Type

Business

Requirements
Must have
• Logo
Business cards
Colour pallette
3D Logo
Nice to have
• Style guide
Designer who can also assist with new Wordpress design
Should not have
• we don't want cheap looking, overtly flashy or gimmicky logo.

```html
<!DOCTYPE html>
<html lang="en">
<head>
<meta charset="utf-8">
<title>Quorvix – Business Card</title>
<link rel="stylesheet" href="https://fonts.googleapis.com/css2?family=Cinzel+Decorative&family=Sorts+Mill+Goudy&family=PT+Sans&display=swap">
<style>
  :root {
    --card-black: #070909;
    --card-deep: #0d1112;
    --text-silver: #c4d0cd;
    --text-shadow: rgba(0, 0, 0, 0.85);
    --tagline-silver: #b9c2c0;
    --divider: #1f2526;
    --mark-fill: #2b3a46;
    --glow: rgba(255, 255, 255, 0.9);
  }
  html, body {
    margin: 0;
    padding: 0;
    width: 1200px;
    height: 686px;
    overflow: hidden;
    background: var(--card-black);
  }
  .card {
    position: relative;
    width: 1200px;
    height: 686px;
    overflow: hidden;
    background:
      radial-gradient(ellipse 170px 260px at 1215px 686px, var(--glow) 0%, rgba(255,255,255,0.35) 30%, rgba(255,255,255,0) 75%),
      radial-gradient(ellipse 900px 600px at 500px 300px, var(--card-deep) 0%, var(--card-black) 80%);
  }
  .brand {
    position: absolute;
    left: 56px;
    top: 40px;
    width: 180px;
    text-align: center;
  }
  .brand-mark {
    display: block;
    margin: 0 auto;
  }
  .brand-name {
    margin-top: 12px;
    font-family: "Sorts Mill Goudy", serif;
    font-size: 26px;
    letter-spacing: 1px;
    color: var(--text-silver);
  }
  .brand-divider {
    position: absolute;
    left: 254px;
    top: 24px;
    width: 1px;
    height: 222px;
    background: var(--divider);
  }
  .tagline {
    position: absolute;
    right: 86px;
    top: 54px;
    margin: 0;
    font-family: "Cinzel Decorative", serif;
    font-weight: 400;
    font-size: 33px;
    line-height: 46px;
    letter-spacing: 1px;
    color: var(--tagline-silver);
    text-shadow: 1px 1px 1px var(--text-shadow), 0 0 1px #ffffff44;
  }
  .tagline span { display: block; }
  .contact {
    position: absolute;
    left: 221px;
    top: 248px;
    margin: 0;
    font-style: normal;
    font-family: "Sorts Mill Goudy", serif;
    font-size: 35px;
    line-height: 46px;
    color: var(--text-silver);
    text-shadow: 2px 2px 2px var(--text-shadow);
  }
  .contact-line { display: block; }
  .contact-phone { display: block; margin-top: 43px; }
  .contact-email {
    position: absolute;
    right: 110px;
    top: 568px;
    font-family: "PT Sans", sans-serif;
    font-size: 33px;
    color: var(--text-silver);
    text-shadow: 2px 2px 2px var(--text-shadow);
  }
  .contact-email .label { margin-right: 12px; }
</style>
</head>
<body>
  <main class="card">
    <div class="brand">
      <svg class="brand-mark" width="150" height="150" viewBox="0 0 150 150" aria-hidden="true">
        <circle cx="75" cy="75" r="72" fill="var(--mark-fill)"/>
      </svg>
      <div class="brand-name">Quorvix</div>
    </div>
    <div class="brand-divider"></div>

    <h2 class="tagline">
      <span>Capturing Business</span>
      <span>Driving Outcomes</span>
    </h2>

    <address class="contact">
      <span class="contact-line">Suite 42</span>
      <span class="contact-line">118 Marlow St</span>
      <span class="contact-line">Sydney, NSW 2000 Australia</span>
      <span class="contact-phone">Phone: (+61) 2 -5550 -1847</span>
    </address>

    <div class="contact-email"><span class="label">Email:</span>Info@quorvix-example.net.au</div>
  </main>
</body>
</html>
```